Business Card for Multi-Brand Sportswear Company

We are looking for a business card which represents our company and the multiple brands within it.

The company: Kelt Athletic (LTD)
The brands: Kelt, PawaLuni, VerdantFlex, Grit and Gale

Employees using these cards would be representing Kelt Athletic, rather than any of the individual brands. You will see a current design within the uploaded files, to give some inspiration. The actual text of the brands is not necessary, but the logos should be on there is some format.

Our creative minds on this are stretched, so we are looking for someone to make this their own, and show us what a good business card should look like.

We may like to get these printed with spot gloss, so keep that in mind with your designs.

www.keltathletic.co.uk

Industry/Entity Type

Business

Contact Information for Business Card

Tom Hollingsworth-Pryce
Operations Manager
(+44) 1632 960 418
Tom@keltathletic.co.uk
www.keltathletic.co.uk

Font styles to use
Sans Serif
Other font styles liked:
• Eurostile

Colors
ffffff

Requirements
Nice to have
• Dark (black) background

```html
<!DOCTYPE html>
<html lang="en">
<head>
<meta charset="utf-8">
<title>Kelt Athletic – Business Card</title>
<link rel="stylesheet" href="https://fonts.googleapis.com/css2?family=Saira:wght@400;500&family=Arimo:wght@400&display=swap">
<style>
  :root {
    --canvas: #d3d3d3;
    --card-black: #060709;
    --panel-grey: #393c42;
    --avatar-blue: #4d5a72;
    --accent-red: #e31e24;
    --white: #ffffff;
    --muted-text: #1f2226;
    --title-text: #0d0e10;
    --edge-teal: #3a7f93;
    --brand-grey: #9a9a9a;
    --brand-plum: #6b5773;
  }
  * { margin: 0; padding: 0; box-sizing: border-box; }
  html, body {
    width: 1167px; height: 1200px; overflow: hidden;
    background: var(--canvas);
  }
  .canvas { position: relative; width: 1167px; height: 1200px; }

  .card {
    position: absolute;
    background: var(--card-black);
    box-shadow: 0 4px 8px rgba(0,0,0,0.35);
    overflow: hidden;
  }

  /* Front */
  .card-front {
    left: 160px; top: 110px; width: 804px; height: 441px;
    border-top: 1px solid var(--edge-teal);
    border-bottom: 1px solid var(--edge-teal);
  }
  .wordmark {
    position: absolute; left: 70px; top: 165px;
    display: flex; align-items: center; gap: 22px;
  }
  .wordmark-dot {
    width: 46px; height: 46px; border-radius: 50%;
    background: var(--accent-red);
  }
  .wordmark-name {
    font-family: "Saira", sans-serif; font-weight: 500;
    font-size: 78px; line-height: 1; letter-spacing: 1px;
    color: var(--white); text-transform: uppercase;
  }
  .tagline {
    position: absolute; right: 38px; top: 258px;
    font-family: "Saira", sans-serif; font-weight: 400;
    font-size: 23px; letter-spacing: 3px;
    color: var(--white); text-transform: uppercase;
  }
  .brand-row {
    position: absolute; left: 474px; top: 370px;
    display: flex; align-items: center; gap: 26px;
    font-family: "Saira", sans-serif; font-weight: 500; font-size: 16px;
  }
  .brand-name { white-space: nowrap; }
  .brand-verdantflex { color: #8a7593; }
  .brand-pawaluni { color: var(--brand-grey); }
  .brand-gritandgale { color: var(--accent-red); }

  /* Back */
  .card-back { left: 156px; top: 615px; width: 811px; height: 449px; }
  .profile-panel {
    position: absolute; left: 0; top: 0; width: 371px; height: 100%;
    background: var(--panel-grey);
  }
  .panel-notch { position: absolute; left: 371px; top: 211px; }
  .avatar {
    position: absolute; left: 95px; top: 142px;
    width: 158px; height: 158px; border-radius: 50%;
    background: radial-gradient(circle at 50% 60%, #6b7891 0%, var(--avatar-blue) 70%);
  }
  .person-name {
    position: absolute; left: 0; width: 371px; top: 314px;
    text-align: center;
    font-family: "Arimo", sans-serif; font-size: 25px;
    color: var(--white);
  }
  .person-title {
    position: absolute; left: 0; width: 371px; top: 350px;
    text-align: center;
    font-family: "Arimo", sans-serif; font-size: 18px;
    color: var(--title-text);
  }
  .contact-list {
    position: absolute; left: 428px; top: 0; list-style: none;
    font-family: "Arimo", sans-serif; font-size: 18px;
    color: var(--muted-text);
  }
  .contact-item {
    position: absolute; left: 0; display: flex; align-items: center;
    gap: 13px; white-space: nowrap;
  }
  .contact-item svg { width: 18px; height: 18px; flex: none; }
  .contact-address { top: 170px; }
  .contact-phone { top: 224px; }
  .contact-email { top: 270px; }
  .contact-web { top: 319px; }
</style>
</head>
<body>
<div class="canvas">

  <section class="card card-front" aria-label="Card front">
    <div class="wordmark">
      <span class="wordmark-dot"></span>
      <span class="wordmark-name">Kelt Athletic</span>
    </div>
    <div class="tagline">Performance Wear</div>
    <div class="brand-row">
      <span class="brand-name brand-verdantflex">VerdantFlex</span>
      <span class="brand-name brand-pawaluni">PawaLuni</span>
      <span class="brand-name brand-gritandgale">Grit and Gale</span>
    </div>
  </section>

  <section class="card card-back" aria-label="Card back">
    <div class="profile-panel">
      <div class="avatar" role="img" aria-label="Profile photo placeholder"></div>
      <div class="person-name">Tom Hollingsworth-Pryce</div>
      <div class="person-title">Operations Manager</div>
    </div>
    <svg class="panel-notch" width="18" height="28" viewBox="0 0 18 28" aria-hidden="true">
      <polygon points="0,0 18,14 0,28" fill="var(--panel-grey)"/>
    </svg>

    <ul class="contact-list">
      <li class="contact-item contact-address">
        <svg viewBox="0 0 18 18" aria-hidden="true"><path d="M9 1a6 6 0 0 0-6 6c0 4.5 6 10 6 10s6-5.5 6-10a6 6 0 0 0-6-6zm0 8.3a2.3 2.3 0 1 1 0-4.6 2.3 2.3 0 0 1 0 4.6z" fill="var(--accent-red)"/></svg>
        <span>Your Address</span>
      </li>
      <li class="contact-item contact-phone">
        <svg viewBox="0 0 18 18" aria-hidden="true"><circle cx="9" cy="9" r="7.5" fill="none" stroke="var(--accent-red)" stroke-width="1.5"/><path d="M6.3 5.2l1.3-.2.8 2-1 .8a5 5 0 0 0 2.8 2.8l.8-1 2 .8-.2 1.3c-3.5.3-6.8-3-6.5-6.5z" fill="var(--accent-red)"/></svg>
        <span>(+44) 1632 960 418</span>
      </li>
      <li class="contact-item contact-email">
        <svg viewBox="0 0 18 18" aria-hidden="true"><rect x="1.5" y="4" width="15" height="10.5" fill="none" stroke="var(--accent-red)" stroke-width="1.4"/><path d="M1.5 4l7.5 6 7.5-6" fill="none" stroke="var(--accent-red)" stroke-width="1.4"/></svg>
        <span>Tom@keltathletic.co.uk</span>
      </li>
      <li class="contact-item contact-web">
        <svg viewBox="0 0 18 18" aria-hidden="true"><g fill="none" stroke="var(--accent-red)" stroke-width="1.3"><circle cx="9" cy="9" r="7.3"/><ellipse cx="9" cy="9" rx="3.2" ry="7.3"/><path d="M1.7 9h14.6M2.8 5.3h12.4M2.8 12.7h12.4"/></g></svg>
        <span>www.keltathletic.co.uk</span>
      </li>
    </ul>
  </section>

</div>
</body>
</html>
```